Non-profit sports organization needs templates for Word and InDesign

"Pelo Minis" is a non-profit organization in Winterthur, which supports the recruitment of young talent by the handball clubs in Winterthur. Every year we run several camps, a tournament for schoolchildren and several handball lessons at school.
During these activities there are always written information. So far we have not given much thought to the design. But since we think that a professional design will also lead to more interaction, we now turn to you as a designer.

For the communication with partners, sponsors, patrons, etc. we need a uniform appearance. Since different departments are currently working with different programs, we need a template for letters and documentation for Word and InDesign.

We will need the documentation template for project descriptions, information, etc.
The letter templates are needed to contact sponsors, authorities, patrons, etc.

Both the letter template and the documentation template should look modern. The design should be based on the existing flyers. Otherwise we have no other requirements so far.

Homepage: www.pelo-minis.ch

Target Market(s)

Letters, documentation or information to authorities, sponsors, associations, patrons, members, participants, etc.

Requirements
Must have
• In addition to the design, the templates should also contain a concept for titles, paragraphs, lists, etc. (colors / fonts / ...)

Word and Indesign templates

```html
<!DOCTYPE html>
<html lang="en">
<head>
<meta charset="utf-8">
<title>Pelo Minis – Letter Template</title>
<link rel="stylesheet" href="https://fonts.googleapis.com/css2?family=Carlito:wght@400;700&family=Oswald:wght@500&family=Arimo&display=swap">
<style>
  :root {
    --backdrop: #d4d5d7;
    --paper: #ffffff;
    --brand-blue: #1ea7e1;
    --brand-red: #e8282b;
    --ink: #4a4a4a;
    --footer-dark: #222222;
    --footer-grey: #e6e6e7;
    --footer-text: #555555;
  }
  * { margin: 0; padding: 0; box-sizing: border-box; }
  html, body {
    width: 1052px; height: 1200px; overflow: hidden;
    background: var(--backdrop);
  }
  .letter {
    position: absolute; left: 62px; top: 0;
    width: 928px; height: 1200px;
    background: var(--paper);
    font-family: "Carlito", "Calibri", sans-serif;
    color: var(--ink);
  }
  .letter__bands { position: absolute; inset: 0; width: 928px; height: 1200px; }
  .brand {
    position: absolute; left: 110px; top: 96px;
    display: flex; align-items: center; gap: 12px;
  }
  .brand__dot { width: 16px; height: 16px; border-radius: 50%; background: var(--brand-red); }
  .brand__name {
    font-family: "Carlito", "Calibri", sans-serif;
    font-weight: 700; font-size: 36px; color: var(--brand-blue);
  }
  .letter__body {
    position: absolute; left: 111px; top: 237px; width: 730px;
    font-size: 15px; line-height: 23.5px;
  }
  .letter__body p { margin-bottom: 24px; }
  .letter__body .date { margin-bottom: 24px; }
  .recipient { margin-bottom: 24px; }
  .highlights { list-style: none; margin: 0 0 24px 30px; }
  .highlights li { position: relative; padding-left: 22px; }
  .highlights li::before {
    content: ""; position: absolute; left: 0; top: 10px;
    width: 5px; height: 5px; border-radius: 50%; background: var(--ink);
  }
  .footer__url {
    position: absolute; left: 196px; top: 1160px; width: 252px;
    text-align: center; font-family: "Oswald", "Arial Narrow", sans-serif;
    font-weight: 500; font-size: 23px; line-height: 30px; color: #ffffff;
    letter-spacing: 0.3px;
  }
  .footer__legal {
    position: absolute; left: 499px; top: 1170px;
    font-family: "Arimo", "Arial", sans-serif; font-size: 11.5px; color: var(--footer-text);
  }
</style>
</head>
<body>
  <main class="letter">
    <svg class="letter__bands" viewBox="0 0 928 1200" aria-hidden="true">
      <polygon class="band-top" points="0,0 368,0 358,10 0,10" fill="var(--brand-blue)"/>
      <polygon class="band-footer-blue" points="569,1148 928,1148 928,1159 559,1159" fill="var(--brand-blue)"/>
      <rect class="band-footer-grey" x="440" y="1159" width="488" height="41" fill="var(--footer-grey)"/>
      <polygon class="band-footer-red" points="0,1172 196,1172 186,1183 0,1183" fill="var(--brand-red)"/>
      <polygon class="band-footer-dark" points="206,1159 476,1159 436,1191 178,1191" fill="var(--footer-dark)"/>
    </svg>

    <div class="brand">
      <span class="brand__dot"></span>
      <span class="brand__name">Pelo Minis</span>
    </div>

    <section class="letter__body">
      <p class="date">Oct 30, 2018</p>
      <address class="recipient" style="font-style:normal">
        Hiring Manager’s Name<br>
        341 Company Address<br>
        Brookvale, California 94301<br>
        (xxx) xxx-xxxx<br>
        hiring.manager@mailbox.example
      </address>
      <p>Dear [Hiring Manager’s Name],</p>
      <p>The first paragraph should contain a self-introduction. You should write who you are, where your<br>expertise lies, where you found the job posting, and why you want to apply for the job.</p>
      <p>The second paragraph should respond directly to the job description written by the hiring manager.<br>Describe how your previous job experiences, skills, and abilities will allow you to meet the company’s<br>needs. To make that easier, you can (and should) literally include words and phrases from the job<br>description in your cover letter.</p>
      <ul class="highlights">
        <li>You can include a bulleted list of your accomplishments</li>
        <li>Make sure you quantify (add numbers to) these bullet points</li>
        <li>A cover letter with numbers is 100% better than one without</li>
      </ul>
      <p>To go the extra mile, do some research about the company, and try to find out what they are doing —<br>and why — given the current state of their industry. Explain how you can fit into that schema, and<br>help push the company forward and achieve any goals you suspect they may have.</p>
      <p>The final paragraph is called the “call to action” portion of your cover letter. Inform them that you’d<br>love to get interviewed. Give them your contact information. Tell them that you’ll be in contact with<br>them in a week if you don’t hear back. Thank them for spending the time to read your cover letter.</p>
      <p>Sincerely,</p>
      <p>Your Name</p>
    </section>

    <div class="footer__url">WWW.PELO-MINIS.CH</div>
    <div class="footer__legal">© Copyright 2019, lorem ipsum dolor sit emet is a dummy text.</div>
  </main>
</body>
</html>
```